Garlic Box Design

This box holds about 20 lbs (about 9 kgs of garlic in small bags inside). It needs to display our logo, barcode, health certificates/permits, and basic company info. It's a rectangular box with the dimensions 20.8 x 9.25 x 7.6 (see the attached drawing for our old box)
Ideally, it should have no more than 3-4 colors, and it would be even better if the color matches our logo colors because printing for each additional color is very expensive. It would be great if the background is either white or brown, because that's the 2 kind of paper we have to make the boxes with.
Company info it should include:
Meadow Acres
Peeled Garlic
Processed in USA
Keep Refrigerated
5 LB X 4
Net WT: 20 LBs

```html
<!DOCTYPE html>
<html lang="en">
<head>
<meta charset="utf-8">
<title>Peeled Garlic Box – Meadow Acres</title>
<link href="https://fonts.googleapis.com/css2?family=Montserrat:wght@500;600;800&display=swap" rel="stylesheet">
<style>
  :root {
    --stage: #e4e4e4;
    --kraft: #b8a479;
    --kraft-flap: #a8956b;
    --white-board: #f3f3f1;
    --white-flap: #e9e9e6;
    --maroon: #4b1b21;
    --green: #3c8c47;
    --lime: #b4c93a;
    --band-text: #a6dca2;
    --band-light: #e8f3e6;
    --hole: #7d7d7d;
  }
  * { box-sizing: border-box; margin: 0; padding: 0; }
  html, body { width: 1067px; height: 1200px; overflow: hidden; }
  body { background: var(--stage); font-family: "Montserrat", sans-serif; color: var(--maroon); }
  .canvas { position: relative; width: 1067px; height: 1200px; }

  .box { position: absolute; left: 38px; width: 991px; height: 404px; }
  .box--kraft { top: 40px; --panel: var(--kraft); --flap: var(--kraft-flap); --seal-fill: #cbb98f; }
  .box--white { top: 640px; --panel: var(--white-board); --flap: var(--white-flap); --seal-fill: #d9cdb5; }

  .flap { position: absolute; left: 0; top: 0; width: 686px; height: 153px; background: var(--flap); border-bottom: 1px solid rgba(0,0,0,.12); }
  .flap__title { position: absolute; right: 40px; top: 58px; font-size: 26px; font-weight: 600; letter-spacing: .5px; }

  .panel { position: absolute; top: 153px; height: 251px; background: var(--panel); overflow: hidden; }
  .panel--front { left: 0; width: 686px; }
  .panel--end { left: 686px; width: 305px; border-left: 1px solid rgba(0,0,0,.12); }

  .band { position: absolute; left: 0; right: 0; bottom: 0; height: 78px; background: var(--green); border-top: 6px solid var(--lime); }
  .band__text { position: absolute; font-size: 13px; font-weight: 500; letter-spacing: .5px; white-space: nowrap; color: var(--band-light); }
  .band__text--pack { left: 22px; top: 22px; }
  .band__text--origin { left: 0; right: 0; top: 26px; text-align: center; font-size: 16px; color: var(--band-text); }
  .band__text--weight { right: 22px; top: 22px; }

  .brand { position: absolute; left: 0; right: 0; top: 28px; display: flex; justify-content: center; align-items: center; gap: 10px; }
  .brand__dot { width: 22px; height: 22px; border-radius: 50%; background: var(--green); }
  .brand__name { font-size: 24px; font-weight: 800; letter-spacing: 1px; text-transform: uppercase; }

  .headline { position: absolute; left: 150px; right: 150px; top: 86px; text-align: center; font-size: 42px; font-weight: 800; letter-spacing: .5px; line-height: 1; white-space: nowrap; }

  .seal { position: absolute; top: 36px; width: 92px; height: 92px; }
  .seal--cold { left: 30px; }
  .seal--quality { right: 30px; border-radius: 50%; border: 2px solid var(--maroon); background: radial-gradient(circle, var(--seal-fill) 0 45%, transparent 46%); }

  .end__title { position: absolute; left: 0; right: 0; top: 26px; text-align: center; font-size: 17px; font-weight: 800; letter-spacing: .5px; }
  .end__handle { position: absolute; left: 92px; top: 58px; width: 120px; height: 34px; border-radius: 17px; background: linear-gradient(180deg, #5f5f5f, var(--hole)); }
  .certs { position: absolute; right: 26px; bottom: 96px; display: flex; gap: 10px; }
  .cert { width: 30px; height: 30px; border-radius: 50%; border: 2px solid var(--maroon); }
</style>
</head>
<body>
<main class="canvas">

  <section class="box box--kraft" aria-label="Kraft board version">
    <div class="flap"><span class="flap__title">Peeled Garlic</span></div>

    <div class="panel panel--front">
      <div class="brand"><span class="brand__dot"></span><span class="brand__name">Meadow Acres</span></div>
      <h1 class="headline">PEELED GARLIC</h1>
      <svg class="seal seal--cold" viewBox="0 0 92 92" aria-label="Keep refrigerated">
        <defs><path id="ring-a" d="M46,46 m-35,0 a35,35 0 1,1 70,0 a35,35 0 1,1 -70,0"/></defs>
        <circle cx="46" cy="46" r="44" fill="none" stroke="#4b1b21" stroke-width="2"/>
        <circle cx="46" cy="46" r="28" fill="none" stroke="#4b1b21" stroke-width="1.2"/>
        <text font-family="Montserrat, sans-serif" font-size="6.5" font-weight="600" fill="#4b1b21" textLength="212" lengthAdjust="spacing"><textPath href="#ring-a">KEEP REFRIGERATED • KEEP REFRIGERATED •</textPath></text>
        <g stroke="#4b1b21" stroke-width="2.4" stroke-linecap="round">
          <line x1="46" y1="30" x2="46" y2="62"/><line x1="32" y1="38" x2="60" y2="54"/><line x1="32" y1="54" x2="60" y2="38"/>
        </g>
      </svg>
      <div class="seal seal--quality" role="img" aria-label="Fresh and peeled garlic, premium quality seal with garlic illustration"></div>
      <div class="band">
        <span class="band__text band__text--pack">5 LB X 4</span>
        <span class="band__text band__text--origin">PROCESSED IN USA</span>
        <span class="band__text band__text--weight">NET WT: 20 LBS</span>
      </div>
    </div>

    <div class="panel panel--end">
      <h2 class="end__title">PEELED GARLIC</h2>
      <div class="end__handle"></div>
      <div class="certs"><span class="cert"></span><span class="cert"></span><span class="cert"></span></div>
      <div class="band">
        <span class="band__text band__text--pack">5 LB X 4</span>
        <span class="band__text band__text--weight">NET WT: 20 LBS</span>
      </div>
    </div>
  </section>

  <section class="box box--white" aria-label="White board version">
    <div class="flap"><span class="flap__title">Peeled Garlic</span></div>

    <div class="panel panel--front">
      <div class="brand"><span class="brand__dot"></span><span class="brand__name">Meadow Acres</span></div>
      <h1 class="headline">PEELED GARLIC</h1>
      <svg class="seal seal--cold" viewBox="0 0 92 92" aria-label="Keep refrigerated">
        <defs><path id="ring-b" d="M46,46 m-35,0 a35,35 0 1,1 70,0 a35,35 0 1,1 -70,0"/></defs>
        <circle cx="46" cy="46" r="44" fill="none" stroke="#4b1b21" stroke-width="2"/>
        <circle cx="46" cy="46" r="28" fill="none" stroke="#4b1b21" stroke-width="1.2"/>
        <text font-family="Montserrat, sans-serif" font-size="6.5" font-weight="600" fill="#4b1b21" textLength="212" lengthAdjust="spacing"><textPath href="#ring-b">KEEP REFRIGERATED • KEEP REFRIGERATED •</textPath></text>
        <g stroke="#4b1b21" stroke-width="2.4" stroke-linecap="round">
          <line x1="46" y1="30" x2="46" y2="62"/><line x1="32" y1="38" x2="60" y2="54"/><line x1="32" y1="54" x2="60" y2="38"/>
        </g>
      </svg>
      <div class="seal seal--quality" role="img" aria-label="Fresh and peeled garlic, premium quality seal with garlic illustration"></div>
      <div class="band">
        <span class="band__text band__text--pack">5 LB X 4</span>
        <span class="band__text band__text--origin">PROCESSED IN USA</span>
        <span class="band__text band__text--weight">NET WT: 20 LBS</span>
      </div>
    </div>

    <div class="panel panel--end">
      <h2 class="end__title">PEELED GARLIC</h2>
      <div class="end__handle"></div>
      <div class="certs"><span class="cert"></span><span class="cert"></span><span class="cert"></span></div>
      <div class="band">
        <span class="band__text band__text--pack">5 LB X 4</span>
        <span class="band__text band__text--weight">NET WT: 20 LBS</span>
      </div>
    </div>
  </section>

</main>
</body>
</html>
```